Mosswood Chiropractic Web Design

We need a fully operating Web site design INCLUDING the code for a Chiropractic Clinic based in Auckland New Zealand to target people from different financial backgrounds.

We need 4 Pages as followed:
1. Home: includes Slideshow of the clinic, General information about chiropractic, option for "Request an appointment", and it would be nice to have a picture on the top right side of the header and the clinic's name and logo on the top left side. on the bottom right we would like a small section for "Testimonial" (A good example: http://www.fernlightstudio.example/ )
(A good example for slide show is: http://www.bektora.example.nz/)
(A good example for the header is: http://www.spinewellpraxis.example/)

2. About Us: this section will include the background information of the company, and a section for our staff (which will includes a photo and description of each person/staff which can be changedanytime)
(a good example: http://www.harbourlanechiro.example.nz/)

3. Contact: includes location, map, contact numbers, email, and a contact box (A good example: http://www.fernlightstudio.example/contact/)

4. Services: includes our products, adjustment equipment, chiropractic products for sale, few pictures of patients while under chiropractic care/adjustment tables

We would also like to add "social networking" options on the bottom left side of every page (Facebook, twitter, Blog, Google+)

Please check the following links to get a feel of our favorite designs:
http://www.spinewellpraxis.example/
http://www.harbourlanechiro.example.nz/
http://www.bektora.example.nz/
http://www.brindlechiropracticclinic.example/
http://www.stillwoven.example.nz/
http://www.pqr.example.nz/index-1.html
http://home.keelbrookchiro.example.nz/home/

we would like to have full access to the back-end- admin of the website to be able to change and add any pictures or texts.
Updates

Hi Lovely Designer,

thank you so much for your proposed designs. We just uploaded the original source file of our logo, for you all to have access on it to facilitate your work. 

Enjoy your day

Orla

Target Market(s)

People with different financial background as well as we are located in the artistic part of town, so appealing to those crowd is important to us.

Industry/Entity Type

Financial

Requirements
Must have
• 1.color similar to the logo or darker colors (Dark and rich colors are prefered)
2. more artistic than a basic doctors' clinic
3. I would like the opening of the web to bring art, tranquility and peaceful images into mind
Should not have
• Not bombarded with lots of info and pics in one page, not too busy and crowded

```html
<!DOCTYPE html>
<html lang="en">
<head>
<meta charset="utf-8">
<title>Mosswood Chiropractic – Professional Chiropractic Care in Auckland</title>
<link href="https://fonts.googleapis.com/css2?family=Montserrat:wght@400;600;700;800&family=Open+Sans:wght@400;600;700&display=swap" rel="stylesheet">
<style>
:root{
  --green:#2cac58;
  --green-dark:#1f8f47;
  --green-title:#27a24f;
  --orange:#f4a21c;
  --blue:#16a5e3;
  --page-bg:#eceef2;
  --card:#ffffff;
  --footer-bg:#f6f7f9;
  --ink:#1d1d1d;
  --muted:#8c9296;
  --line:#e3e5e8;
  --field:#f3f4f5;
}
*{margin:0;padding:0;box-sizing:border-box}
html,body{width:793px;height:1200px;overflow:hidden;background:var(--page-bg)}
body{font-family:"Open Sans",Arial,sans-serif;color:var(--ink)}
.page{position:relative;width:800px;height:1210px;transform:scale(0.99125,0.99174);transform-origin:0 0;background:var(--page-bg)}
.abs{position:absolute}

/* hero */
.hero-photo{left:0;top:0;width:800px;height:326px;background:linear-gradient(100deg,#4c7a2a 0%,#7fa444 30%,#a9c65e 50%,#6d9a3a 72%,#3f6b22 100%)}
.topbar{left:0;top:0;width:800px;height:41px;background:var(--green)}
.brand{left:122px;top:0;width:144px;height:64px;background:#fff;box-shadow:0 2px 6px rgba(0,0,0,.25);display:flex;align-items:center;justify-content:center;gap:6px}
.brand-mark{width:10px;height:10px;border-radius:50%;background:var(--green)}
.brand-name{font-family:"Montserrat",sans-serif;font-weight:600;font-size:11px;color:var(--green-dark);line-height:1.1;text-align:left}
.nav{right:80px;top:20px;display:flex;gap:11px;align-items:center;white-space:nowrap}
.nav a{font-family:"Montserrat",sans-serif;font-size:7px;font-weight:700;color:#fff;text-decoration:none;text-transform:uppercase}
.nav a.cta{border:1px solid #bfe8cc;background:var(--green-dark);padding:3px 5px;border-radius:3px}
.hero-title{left:136px;top:95px;font-family:"Montserrat",sans-serif;font-weight:800;font-size:28px;line-height:29px;color:#fff;text-shadow:0 1px 3px rgba(0,0,0,.35)}
.hero-text{left:137px;top:158px;width:285px;font-family:"Montserrat",sans-serif;font-weight:700;font-size:11px;line-height:16.5px;color:#fff;text-shadow:0 1px 2px rgba(0,0,0,.4)}
.pill{display:inline-flex;align-items:center;justify-content:center;background:var(--green);color:#fff;font-family:"Montserrat",sans-serif;font-weight:600;font-size:7.5px;border-radius:10px;text-transform:uppercase}
.hero-btn{left:137px;top:233px;width:70px;height:17px}

/* intro */
.card{background:var(--card);border-radius:6px;box-shadow:0 1px 3px rgba(0,0,0,.08)}
.intro{left:114px;top:291px;width:587px;height:127px;text-align:center}
.intro h1{margin-top:15px;font-family:"Montserrat",sans-serif;font-weight:600;font-size:15px;color:var(--green-title)}
.intro p{margin:5px auto 0;width:490px;font-family:"Open Sans",Arial,sans-serif;font-weight:700;font-size:8.3px;line-height:12.5px;letter-spacing:-0.1px;color:var(--muted)}
.appt{left:133px;top:84px;width:146px;height:24px;background:var(--orange);color:#fff;font-family:"Montserrat",sans-serif;font-weight:700;font-size:9px;border-radius:3px;display:flex;align-items:center;justify-content:center}
.or{left:290px;top:86px;font-family:"Montserrat",sans-serif;font-weight:700;font-size:14px;color:#9aa0a4}
.phone{left:319px;top:85px;font-family:"Montserrat",sans-serif;font-weight:600;font-size:15px;color:var(--ink)}

/* main */
.main{left:114px;top:427px;width:587px;height:521px}
.vline{width:1px;background:var(--line)}
.hline{height:1px;background:var(--line)}
.col-title{font-family:"Montserrat",sans-serif;font-weight:700;font-size:8.5px;text-transform:uppercase;color:var(--ink)}
.thumb{border-radius:6px}
.small{font-size:7px;line-height:10.5px;color:var(--muted)}
.aside-title{font-family:"Montserrat",sans-serif;font-weight:700;font-size:9.5px;line-height:13px;color:var(--ink)}
.aside-text{font-size:7px;line-height:10.5px;color:var(--muted)}
.aside-text b{color:var(--ink)}
.form-title{font-family:"Montserrat",sans-serif;font-weight:700;font-size:8.5px}
.label{font-size:7px;color:var(--ink)}
.field{background:var(--field);border:1px solid #e6e8ea}
.sum{font-family:"Montserrat",sans-serif;font-weight:800;font-size:14px}
.callback{background:var(--blue);color:#fff;font-family:"Montserrat",sans-serif;font-weight:600;font-size:8.5px;border-radius:12px;display:flex;align-items:center;justify-content:center}

.doc-title{font-family:"Montserrat",sans-serif;font-weight:700;font-size:11.5px;line-height:15px}
.doc-text{width:183px;font-size:6.4px;line-height:10px;color:#444;text-align:justify}
.doc-text p{margin-bottom:7px}
.pain-box{left:330px;top:626px;width:160px;height:276px;border:1.5px solid #9ad9ae;border-radius:6px;background:#fff}
.pain-box h2{margin:8px 10px 0;text-align:center;font-family:"Montserrat",sans-serif;font-weight:700;font-size:11.5px;line-height:14px}
.pain-box h3{margin:15px 0 0 18px;font-family:"Montserrat",sans-serif;font-weight:700;font-size:8px}
.ticks{list-style:none;margin:7px 0 0 14px}
.ticks li{display:flex;align-items:center;gap:9px;height:14.5px;font-size:7px;color:#333}
.ticks svg{flex:none}

/* footer */
.footer{left:114px;top:960px;width:587px;height:137px;background:var(--footer-bg);border-radius:6px}
.f-head{font-family:"Montserrat",sans-serif;font-weight:700;font-size:7px;text-transform:uppercase}
.f-list{list-style:none;margin-top:8px}
.f-list li{font-size:6.2px;line-height:11.2px;color:#333}
.nl-field{width:127px;height:19px;background:#fff;border:1px solid #dcdfe2;font-size:6.5px;color:#9aa0a4;display:flex;align-items:center;padding-left:6px}
.nl-btn{width:38px;height:19px;background:var(--blue);color:#fff;font-family:"Montserrat",sans-serif;font-weight:600;font-size:7px;display:flex;align-items:center;justify-content:center}
.social{display:flex;gap:3px}
.social span{width:11px;height:11px;border-radius:1px}
.copy{font-family:"Montserrat",sans-serif;font-weight:700;font-size:6.5px}
</style>
</head>
<body>
<div class="page">

  <div class="abs hero-photo" role="img" aria-label="Photo of a smiling couple on bicycles in a green leafy park"></div>
  <div class="abs topbar"></div>
  <div class="abs brand"><span class="brand-mark"></span><span class="brand-name">Mosswood<br>Chiropractic</span></div>
  <nav class="abs nav">
    <a href="#">Home</a><a href="#">About Us</a><a href="#">Services</a><a href="#">Meet the Doctor</a><a href="#" class="cta">Schedule an Appointment</a><a href="#">Contact Us</a>
  </nav>
  <h1 class="abs hero-title">Helping you<br>achieve your best.</h1>
  <p class="abs hero-text">Enjoying a long and healthy life is important to everyone. Chiropractic care unlocks your body's true potential and natural healing process to ensure your life is a healthy life.</p>
  <a class="abs pill hero-btn">Read More</a>

  <section class="abs card intro">
    <h1>Mosswood - Professional Chiropractic Care in Auckland</h1>
    <p>Is pain, injury or stress preventing you from being yourself? Mosswood Chiropractor's experienced chiropractic care can bring you back to a healthy life. . We can help you regain the quality of life you may have been missing with our non-invasive, drug free treatment, in a professional and familiar environment.</p>
    <a class="abs appt">Schedule an Appointment</a>
    <span class="abs or">or</span>
    <span class="abs phone">(09) 555 0142</span>
  </section>

  <section class="abs card main"></section>
  <div class="abs vline" style="left:310px;top:427px;height:184px"></div>
  <div class="abs vline" style="left:506px;top:427px;height:521px"></div>
  <div class="abs hline" style="left:114px;top:610px;width:392px"></div>

  <h2 class="abs col-title" style="left:129px;top:439px">Safe &amp; Effective Chiropractic</h2>
  <div class="abs thumb" style="left:127px;top:455px;width:162px;height:67px;background:linear-gradient(90deg,#d9d4cc,#efe9e0 60%,#e4d8c6)" role="img" aria-label="Photo of a chiropractor consulting with an older patient"></div>
  <p class="abs small" style="left:128px;top:531px;width:162px">Chiropractic care is a safe, effective and natural approach to managing pain and other health related issues. We invite you for a complimentary, no obligation consultation today.</p>
  <a class="abs pill" style="left:127px;top:580px;width:70px;height:17px">Read More</a>

  <h2 class="abs col-title" style="left:321px;top:439px">Live Better Today!</h2>
  <div class="abs thumb" style="left:321px;top:455px;width:179px;height:67px;background:linear-gradient(90deg,#8fa760,#c2cf8c 50%,#7e9a4c)" role="img" aria-label="Photo of a couple cycling through tall grass"></div>
  <p class="abs small" style="left:323px;top:531px;width:162px">Enjoying a long and healthy life is important to everyone. Chiropractic care unlocks your body's true potential and natural healing process to ensure your life is a healthy life.</p>
  <a class="abs pill" style="left:323px;top:577px;width:70px;height:17px">Read More</a>

  <h2 class="abs aside-title" style="left:516px;top:437px;width:170px">Choosing the right Chiropractor is an important choice to make.</h2>
  <p class="abs aside-text" style="left:516px;top:466px;width:160px">If you are new to chiropractic care, this site can provide some answers to your most basic questions - just go to our <b>Frequently Asked Questions</b> and you can learn how simple, safe and comfortable chiropractic treatment is and how it can improve your quality of life.</p>

  <h2 class="abs form-title" style="left:516px;top:564px">Talk to Our Experts</h2>
  <span class="abs label" style="left:516px;top:585px">Name</span>
  <div class="abs field" style="left:516px;top:597px;width:170px;height:20px"></div>
  <span class="abs label" style="left:516px;top:622px">E-Mail Address</span>
  <div class="abs field" style="left:516px;top:633px;width:170px;height:20px"></div>
  <span class="abs label" style="left:516px;top:659px">Phone Number</span>
  <div class="abs field" style="left:516px;top:670px;width:170px;height:20px"></div>
  <span class="abs label" style="left:516px;top:696px">Message to Dr Mosswood</span>
  <div class="abs field" style="left:516px;top:708px;width:170px;height:69px"></div>
  <p class="abs aside-text" style="left:518px;top:783px;width:170px;color:#444">We hate spam too. Do the sum or addition below to prove you are human</p>
  <span class="abs sum" style="left:517px;top:815px">5+6 =</span>
  <a class="abs callback" style="left:515px;top:846px;width:172px;height:23px">Request a Call Back</a>
  <p class="abs aside-text" style="left:515px;top:880px;width:172px;text-align:center;color:#9aa0a4">We hate spam too. Do the sum or addition below to prove you are human</p>

  <h2 class="abs doc-title" style="left:134px;top:626px">Dr Mosswood - Building<br>a Better Care....</h2>
  <div class="abs doc-text" style="left:134px;top:667px">
    <p>Lorem ipsum dolor sit amet, consectetur adipiscing elit. Suspendisse tristique adipiscing risus. Curabitur aliquet nunc nulla, ut luctus ante malesuada ac. Integer molestie adipiscing elit, sit amet vulputate erat ullamcorper nec.</p>
    <p>Donec condimentum justo sit amet sapien auctor scelerisque. Cras pellentesque quis orci imperdiet feugiat. Donec erat ipsum, accumsan non tincidunt eu, rutrum et massa. Vestibulum eleifend molestie diam. Nunc eget mattis ante. Donec placerat blandit euismod.</p>
    <p style="margin-top:12px">Morbi iaculis quam non urna hendrerit dapibus. Fusce varius justo tincidunt est dignissim, eu euismod lectus tincidunt. Class aptent taciti sociosqu ad litora torquent per conubia nostra, per inceptos himenaeos. Nam ultricies orci ac dolor tincidunt lobortis. Proin metus mauris, elementum in lacus ac, euismod pharetra nisi. Curabitur vehicula sit amet ligula tincidunt scelerisque. Nulla elementum sem tincidunt arcu aliquam ornare. Aliquam luctus quam arcu, id scelerisque ligula lobortis sit amet. Nulla aliquam turpis in vehicula interdum. Donec a lobortis orci.</p>
  </div>
  <a class="abs pill" style="left:134px;top:886px;width:70px;height:17px">Read More</a>

  <aside class="abs pain-box">
    <h2>Don't allow pain to limit your lifestyle.</h2>
    <h3>Do you suffer from...</h3>
    <ul class="ticks">
      <li><svg width="10" height="10" viewBox="0 0 10 10"><circle cx="5" cy="5" r="5" fill="#2cac58"/><path d="M2.6 5.2l1.6 1.6 3.2-3.4" fill="none" stroke="#fff" stroke-width="1.3"/></svg>Sports Injuries</li>
      <li><svg width="10" height="10" viewBox="0 0 10 10"><circle cx="5" cy="5" r="5" fill="#2cac58"/><path d="M2.6 5.2l1.6 1.6 3.2-3.4" fill="none" stroke="#fff" stroke-width="1.3"/></svg>Degenerative Joint Pain</li>
      <li><svg width="10" height="10" viewBox="0 0 10 10"><circle cx="5" cy="5" r="5" fill="#2cac58"/><path d="M2.6 5.2l1.6 1.6 3.2-3.4" fill="none" stroke="#fff" stroke-width="1.3"/></svg>Sciatica/Back Pain</li>
      <li><svg width="10" height="10" viewBox="0 0 10 10"><circle cx="5" cy="5" r="5" fill="#2cac58"/><path d="M2.6 5.2l1.6 1.6 3.2-3.4" fill="none" stroke="#fff" stroke-width="1.3"/></svg>Auto Accidents</li>
      <li><svg width="10" height="10" viewBox="0 0 10 10"><circle cx="5" cy="5" r="5" fill="#2cac58"/><path d="M2.6 5.2l1.6 1.6 3.2-3.4" fill="none" stroke="#fff" stroke-width="1.3"/></svg>Neck Pain/Headaches</li>
      <li><svg width="10" height="10" viewBox="0 0 10 10"><circle cx="5" cy="5" r="5" fill="#2cac58"/><path d="M2.6 5.2l1.6 1.6 3.2-3.4" fill="none" stroke="#fff" stroke-width="1.3"/></svg>Carpal Tunnel Syndrome</li>
      <li><svg width="10" height="10" viewBox="0 0 10 10"><circle cx="5" cy="5" r="5" fill="#2cac58"/><path d="M2.6 5.2l1.6 1.6 3.2-3.4" fill="none" stroke="#fff" stroke-width="1.3"/></svg>Shoulder Pain</li>
      <li><svg width="10" height="10" viewBox="0 0 10 10"><circle cx="5" cy="5" r="5" fill="#2cac58"/><path d="M2.6 5.2l1.6 1.6 3.2-3.4" fill="none" stroke="#fff" stroke-width="1.3"/></svg>Herniated or Bulging Discs</li>
      <li><svg width="10" height="10" viewBox="0 0 10 10"><circle cx="5" cy="5" r="5" fill="#2cac58"/><path d="M2.6 5.2l1.6 1.6 3.2-3.4" fill="none" stroke="#fff" stroke-width="1.3"/></svg>Plantar Fascitis</li>
      <li><svg width="10" height="10" viewBox="0 0 10 10"><circle cx="5" cy="5" r="5" fill="#2cac58"/><path d="M2.6 5.2l1.6 1.6 3.2-3.4" fill="none" stroke="#fff" stroke-width="1.3"/></svg>Upper and Lower Exremity Injuries</li>
      <li><svg width="10" height="10" viewBox="0 0 10 10"><circle cx="5" cy="5" r="5" fill="#2cac58"/><path d="M2.6 5.2l1.6 1.6 3.2-3.4" fill="none" stroke="#fff" stroke-width="1.3"/></svg>Vertigo/Dizziness</li>
      <li><svg width="10" height="10" viewBox="0 0 10 10"><circle cx="5" cy="5" r="5" fill="#2cac58"/><path d="M2.6 5.2l1.6 1.6 3.2-3.4" fill="none" stroke="#fff" stroke-width="1.3"/></svg>Childhood Ear Infections</li>
    </ul>
  </aside>

  <footer class="abs footer"></footer>
  <div class="abs" style="left:130px;top:973px">
    <h4 class="f-head">Our Team</h4>
    <ul class="f-list"><li>About Us</li><li>Our Team</li><li>Testimonials</li><li>News &amp; Announcements</li><li>Special Offers</li></ul>
  </div>
  <div class="abs" style="left:228px;top:973px">
    <h4 class="f-head">Our Services</h4>
    <ul class="f-list"><li>Sports Injuries</li><li>Degenerative Joint Pain</li><li>Sciatica/Back Pain</li><li>Auto Accidents</li><li>Neck Pain/Headaches</li><li>Carpal Tunnel Syndrome</li></ul>
  </div>
  <ul class="abs f-list" style="left:322px;top:979px"><li>Shoulder Pain</li><li>Herniated or Bulging Discs</li><li>Plantar Fascitis</li><li>Upper and Lower Exremity Injuries</li><li>Vertigo/Dizziness</li><li>Childhood Ear Infections</li></ul>
  <div class="abs" style="left:438px;top:973px;line-height:12.5px">
    <h4 class="f-head">FAQ's</h4><h4 class="f-head">Blog</h4><h4 class="f-head">Contact Us</h4>
  </div>
  <h4 class="abs f-head" style="left:518px;top:973px">Subscribe to our montly newsletter</h4>
  <div class="abs nl-field" style="left:518px;top:988px">your email address</div>
  <a class="abs nl-btn" style="left:645px;top:988px">Sign Up</a>
  <h4 class="abs f-head" style="left:518px;top:1024px">Follow us in social media</h4>
  <div class="abs social" style="left:518px;top:1037px">
    <span style="background:#dd4b39"></span><span style="background:#cb2027"></span><span style="background:#0e76a8"></span><span style="background:#d8d8d8"></span><span style="background:#3b5998"></span><span style="background:#2ba9e1"></span>
  </div>
  <p class="abs copy" style="left:131px;top:1078px">Copyright © Mosswood - Professional Chiropractic Care in Auckland</p>

</div>
</body>
</html>
```